Taking a Paper and turning into a wonderful White Paper for Prospects and Clients

This is a white paper I need designed. I am including my company brochure so you can see the design/fonts being used and I'm including a white paper created - one that I like very much.

I am "NOT" looking for a cookie cutter white paper. I'm looking for a nice, clean design but with some creativity. Check out the white paper I included and you will get the idea.

Also included:
- the paper to be designed
- the paper to be designed "WITH" suggested design features such as carve outs, call outs and such

A few things I "DO NOT" like:
- images that are cheesy or corny
* people sitting at a table in a meeting
* Buildings

The white paper I included did not use pictures but had more design created by the firm. I like this approach and will probably give something like this more weight but is not required.
Updates

Reason: Realized time frame was too tight

Target Market(s)

Higher-End, wealthier clients

Industry/Entity Type

It Company

Requirements
Must have
• I DO NOT want the copy to be bunched together. The layout should flow where the copy is broken in the right spots to make reading easier. If you read a paper and it is just copy, interest is lost by everyone.
• COLORS: you can see from what I have included the colors I use
• My preference are very balanced colors using "clean spacing"

```html
<!DOCTYPE html>
<html lang="en">
<head>
<meta charset="utf-8">
<title>Verantio – White Paper, Page 2</title>
<link rel="stylesheet" href="https://fonts.googleapis.com/css2?family=Montserrat:wght@700;800&family=Noto+Serif:wght@400&display=swap">
<style>
  :root {
    --ink: #24365f;
    --rule: #5a6a8a;
    --page: #ffffff;
    --folio: #111111;
  }
  html, body {
    margin: 0;
    padding: 0;
    width: 927px;
    height: 1200px;
    overflow: hidden;
    background: var(--page);
  }
  .page {
    position: relative;
    width: 927px;
    height: 1200px;
    background: var(--page);
    color: var(--ink);
  }
  .running-head {
    position: absolute;
    left: 124px;
    top: 55px;
    margin: 0;
    font-family: "Montserrat", sans-serif;
    font-weight: 700;
    font-size: 10px;
    letter-spacing: 0.02em;
    color: var(--ink);
  }
  .pull-quote {
    position: absolute;
    margin: 0;
    font-family: "Noto Serif", serif;
    font-weight: 400;
    color: var(--ink);
  }
  .pull-quote--opening {
    left: 124px;
    top: 156px;
    width: 380px;
    font-size: 31px;
    line-height: 43px;
  }
  .pull-quote--closing {
    right: 143px;
    top: 906px;
    width: 400px;
    text-align: right;
    font-size: 29px;
    line-height: 40px;
  }
  .rule {
    position: absolute;
    height: 1px;
    background: var(--rule);
  }
  .rule--opening { left: 421px; top: 179px; width: 392px; }
  .rule--closing { left: 137px; top: 931px; width: 242px; }
  .folio {
    position: absolute;
    left: 800px;
    top: 1127px;
    margin: 0;
    font-family: "Montserrat", sans-serif;
    font-weight: 800;
    font-size: 13px;
    color: var(--folio);
  }
</style>
</head>
<body>
  <main class="page">
    <p class="running-head">VERANTIO –</p>

    <p class="pull-quote pull-quote--opening">Well, we say, the<br>question is not<br>whether your financial<br>advisor is a fiduciary.</p>
    <div class="rule rule--opening"></div>

    <div class="rule rule--closing"></div>
    <p class="pull-quote pull-quote--closing">The question is whether<br>your financial advisor is<br>consistently acting in<br>your best interest.</p>

    <p class="folio">2</p>
  </main>
</body>
</html>
```